Lumen Grove Lead Generator + Checklist

I have typed up a 9 page word doc to be a lead generator for my website called "7 Hidden Traps Gathering Hosts Overlook" and I am looking for someone to clean it up, and make it professional and inline with our brand.

Logo Hex: #971F20

Industry/Entity Type

Event Planning

Font styles to use
Other font styles liked:
• Helvetica Neue is our brands font, but it doesn't have to be that. Something similar that is rounded would be good like Arial I think.

Requirements
Must have
• Clean, but elegant design.
• Because it is very text heavy, have the topics easily broken out and maybe staggered so that it is easy to identify main topics and sub topics.
Should not have
• Not just looking for basic formating around the edges of the document, but to also have the text displayed in an easily readable way with clear sections.

```html
<!DOCTYPE html>
<html lang="en">
<head>
<meta charset="utf-8">
<title>Lumen Grove – Recap &amp; Event Planning Checklist</title>
<link rel="stylesheet" href="https://fonts.googleapis.com/css2?family=Inter:ital,wght@0,300;0,400;0,600;0,700;1,400&display=swap">
<style>
  :root {
    --brand: #971F20;
    --ink: #1c1c1c;
    --link: #1a4fd6;
    --paper: #ffffff;
  }
  * { box-sizing: border-box; margin: 0; padding: 0; }
  html, body { width: 1200px; height: 777px; overflow: hidden; background: var(--paper); }
  body { font-family: "Inter", Arial, sans-serif; color: var(--ink); position: relative; }

  .page-title {
    font-weight: 300; color: var(--brand); font-size: 24px; letter-spacing: -0.3px;
    text-transform: uppercase; line-height: 1;
  }

  /* Left spread page */
  .recap-page { position: absolute; left: 34px; top: 60px; width: 526px; }
  .recap-intro { margin-top: 14px; font-size: 11.2px; line-height: 13.6px; }
  .recap-heading { margin-top: 14px; font-size: 11.2px; font-weight: 700; }
  .recap-list { margin: 5px 0 0 18px; list-style: none; counter-reset: step; }
  .recap-list li { counter-increment: step; font-size: 11.2px; line-height: 19.2px; position: relative; padding-left: 17px; }
  .recap-list li::before { content: counter(step) "."; position: absolute; left: 0; color: var(--brand); font-weight: 700; }
  .recap-ps { margin-top: 14px; font-size: 11.2px; }
  .recap-ps strong { font-weight: 700; }
  .recap-thanks { margin: 13px 0 0 17px; font-size: 11.2px; line-height: 13.6px; font-style: italic; width: 500px; }

  /* Right spread page */
  .checklist-page { position: absolute; left: 640px; top: 60px; width: 530px; }
  .checklist-page .page-title { text-align: center; margin-left: 0; padding-left: 0; }
  .checklist-sub { text-align: center; font-weight: 700; font-size: 12px; line-height: 15.5px; margin-top: 2px; }
  .checklist-col { position: absolute; top: 85px; width: 250px; }
  .checklist-col.first { left: 2px; }
  .checklist-col.second { left: 277px; }
  .task-group + .task-group { margin-top: 11px; }
  .task-group h3 { font-size: 10.4px; font-weight: 600; margin-bottom: 4px; }
  .task-list { list-style: none; margin-left: 18px; }
  .task-list li { position: relative; padding-left: 17px; font-size: 10.4px; line-height: 11.6px; margin-bottom: 3px; width: 212px; }
  .task-list li::before {
    content: ""; position: absolute; left: 0; top: 2px; width: 6px; height: 6px;
    border: 1px solid var(--ink); box-shadow: 1.5px 1.5px 0 var(--ink);
  }
  .task-list a { color: var(--link); text-decoration: underline; }

  /* Footers */
  .page-footer { position: absolute; top: 741px; font-size: 7.4px; display: flex; align-items: center; gap: 6px; }
  .page-footer.left { left: 14px; }
  .page-footer.right { right: 12px; }
  .footer-mark { width: 13px; height: 13px; background: var(--brand); }
  .page-number { color: var(--brand); font-weight: 700; }
</style>
</head>
<body>

<section class="recap-page">
  <h1 class="page-title">Congrats!</h1>
  <p class="recap-intro">You’re on your way to planning an event that people will talk about for years and in a <strong>good way</strong>. You won’t have your name associated with an event where the room was too small or the food was cold, and you can be confident that you’ve planned a great event by selecting the best possible venue.</p>
  <h2 class="recap-heading">To recap</h2>
  <ol class="recap-list">
    <li>Know the type of event you’re planning</li>
    <li>Don’t just know your event - know your audience</li>
    <li>Ask the venue the <em>right</em> questions</li>
    <li>Plan the food and drinks - that’s why everyone is coming in the first place</li>
    <li>Lastly, Don’t take anything for granted</li>
  </ol>
  <p class="recap-ps"><strong>P.S.</strong> Be on the lookout for an event planning checklist that I’ll be sending you in a couple days!</p>
  <p class="recap-thanks">A special thanks to Marisa Delacourt, Dana Whitlow, Mina Hollister and Avery Brandt who helped put this guide together. Collectively they have been planning events for over a decade that have brought our community closer together.</p>
</section>

<section class="checklist-page">
  <h1 class="page-title">Event Planning Checklist</h1>
  <p class="checklist-sub">Every event is unique, but this should help serve as a general checklist for<br>most events.</p>

  <div class="checklist-col first">
    <div class="task-group">
      <h3>As Early As Possible</h3>
      <ul class="task-list">
        <li>Number of guests</li>
        <li>Date(s) for the event (Factor in your speakers schedule if necessary)</li>
        <li>General location</li>
        <li>Type of venue (Casual vs Formal, Indoor vs Outdoor, Quiet private room vs Open area)</li>
        <li>Develop an initial budget</li>
      </ul>
    </div>
    <div class="task-group">
      <h3>Book Your Venue</h3>
      <ul class="task-list">
        <li>Go to <a href="#">www.lumengrove-venues.com</a> to compare venues.</li>
      </ul>
    </div>
    <div class="task-group">
      <h3>Confirm Event Details</h3>
      <ul class="task-list">
        <li>Confirm your speaker(s) and any remaining marketing details with them</li>
        <li>Coordinate relevant details with the venue like what will be served, timing, etc.</li>
        <li>Set up event on social media and/or Ticketnest if using that platform</li>
      </ul>
    </div>
    <div class="task-group">
      <h3>Notify Your Guests</h3>
      <ul class="task-list">
        <li>Email your guests</li>
        <li>Post the event to social media (Huddlehub, Chatterloop, Snapwall, etc)</li>
        <li>Send out more formal invites if necessary</li>
      </ul>
    </div>
    <div class="task-group">
      <h3>Coordinate With Vendors</h3>
      <ul class="task-list">
        <li>Photographer</li>
        <li>Food</li>
        <li>Beverages</li>
        <li>Music (DJ, Band, etc)</li>
        <li>Audio/Visual Support</li>
        <li>Decorations</li>
        <li>Glassware/attendee gifts</li>
        <li>Child Care</li>
        <li>Tables and chairs</li>
        <li>Linens</li>
      </ul>
    </div>
  </div>

  <div class="checklist-col second">
    <div class="task-group">
      <h3>Military Specific Considerations</h3>
      <ul class="task-list">
        <li>Identify the Color Guard</li>
        <li>Coordinate with the units band</li>
        <li>Coordinate with the protocol office if senior leaders are attending</li>
        <li>Coordinate with PAO</li>
        <li>Conduct any necessary legal reviews</li>
      </ul>
    </div>
    <div class="task-group">
      <h3>Execution</h3>
      <ul class="task-list">
        <li>Check up on marketing and ticket sales/ attendees and see if you need to adjust anything</li>
        <li>Reconfirm budget based off of the updated number of guests</li>
        <li>Organize speaker gifts</li>
        <li>VIP travel coordination</li>
      </ul>
    </div>
    <div class="task-group">
      <h3>1 Week Prior to the Event</h3>
      <ul class="task-list">
        <li>Re-confirm the venue and update them on any changes to guest count</li>
        <li>Re-confirm all speakers</li>
        <li>Re-confirm all vendors</li>
        <li>Ensure the budget is matching up</li>
        <li>Print necessary materials (programs, name tags, name tents, etc)</li>
        <li>Contact attendees with the update agenda and key information like when and where the event starts, attire, if they should bring their ticket, parking instructions, directions, special instructions, etc.</li>
        <li>Develop the script and confirm the bios match up and all participants understand and have practiced their part (if necessary)</li>
        <li>Conduct venue walk through</li>
      </ul>
    </div>
    <div class="task-group">
      <h3>Day Before</h3>
      <ul class="task-list">
        <li>Re-confirm all details</li>
      </ul>
    </div>
    <div class="task-group">
      <h3>After</h3>
      <ul class="task-list">
        <li>Coordinate payment if necessary</li>
        <li>Facilitate lost and found between the venue and guests if necessary</li>
      </ul>
    </div>
  </div>
</section>

<footer class="page-footer left">
  <span class="footer-mark"></span>
  <span><span class="page-number">8</span> | Lumen Grove</span>
</footer>
<footer class="page-footer right">
  <span>7 Hidden Traps Gathering Hosts Overlook &nbsp;| <span class="page-number">9</span></span>
  <span class="footer-mark"></span>
</footer>

</body>
</html>
```